HIGH-END ANTI AGING START-UP NEEDS DOCUMENT/LETTERHEAD DESIGN!!!!

We are a high end anti-aging and health start-up catering to clients in Stamford and NYC. We just did a logo redesign and are now looking for a letter head design that we can use IN GOOGLE DOCS for marwickcaregroup.example clients. We are REALLY EXCITED to see what you can show us!!!!!!!! We need something sophisticated and MODERN! Thanks so much!

Target Market(s)

High end, boutique medical clients. Our clientele is fairly high profile and we need a sleek, sophisticated letter head to put on all of our marketing materials and medical forms as well.

Industry/Entity Type

Medical

Font styles to use
Serif
Sans Serif

Colors
0255a3
ffffff
00a990
1b1b1b
919191

Requirements
Must have
• Must have the logo and "Marwick Care Group" written somewhere. Must have our URL www.marwickcaregroup.example.
Nice to have
• office phone number (203) 555-0147
Should not have
• Colors outside of our logo colors + grey + black

```html
<!DOCTYPE html>
<html lang="en">
<head>
<meta charset="utf-8">
<title>Marwick Care Group — Letterhead</title>
<link rel="stylesheet" href="https://fonts.googleapis.com/css2?family=Libre+Baskerville:wght@700&family=Open+Sans:wght@400;600&display=swap">
<style>
  :root {
    --backdrop: #b9cfe6;
    --paper: #ffffff;
    --brand-blue: #5a8ff0;
    --brand-green: #5f9e1f;
    --logo-green: #1e9a4a;
    --logo-blue: #3a6fe0;
    --tint-blue: #e4ecfb;
    --tint-green: #e6f4ec;
    --text-grey: #777777;
  }
  * { margin: 0; padding: 0; box-sizing: border-box; }
  html, body {
    width: 1200px;
    height: 784px;
    overflow: hidden;
    background: var(--backdrop);
  }
  .letterhead {
    position: absolute;
    left: 338px;
    top: 22px;
    width: 523px;
    height: 740px;
    background: var(--paper);
    box-shadow: 0 6px 18px rgba(40, 80, 130, 0.25);
    overflow: hidden;
  }
  .bar { position: absolute; height: 6px; }
  .bar--top-left { left: 0; top: 12px; width: 42px; background: var(--brand-blue); }
  .bar--header-green { left: 180px; top: 92px; width: 124px; background: var(--brand-green); }
  .bar--header-blue { left: 440px; top: 150px; width: 70px; background: var(--brand-blue); }
  .bar--footer-blue { left: 0; bottom: 6px; width: 360px; height: 8px; background: var(--brand-blue); }
  .bar--footer-green { left: 370px; bottom: 6px; width: 153px; height: 8px; background: var(--brand-green); }

  .brand {
    position: absolute;
    left: 30px;
    top: 40px;
    display: flex;
    align-items: center;
    gap: 10px;
  }
  .brand__mark {
    width: 30px;
    height: 30px;
    border-radius: 50%;
    background: var(--logo-green);
  }
  .brand__name {
    font-family: "Libre Baskerville", Georgia, serif;
    font-weight: 700;
    font-size: 15px;
    color: var(--logo-blue);
    letter-spacing: 0.3px;
  }

  .tint {
    position: absolute;
    background: var(--tint-blue);
  }
  .tint--a { left: 420px; top: 70px; width: 60px; height: 40px; }
  .tint--b { left: 470px; top: 95px; width: 53px; height: 45px; }
  .tint--c { left: 400px; top: 118px; width: 52px; height: 30px; }
  .tint--d { left: 430px; top: 160px; width: 75px; height: 52px; }

  .contact {
    position: absolute;
    left: 316px;
    top: 80px;
    list-style: none;
    font-family: "Open Sans", Arial, sans-serif;
    font-size: 8.5px;
    line-height: 13px;
    color: var(--text-grey);
  }
  .contact__item { display: flex; align-items: flex-start; gap: 5px; }
  .contact__icon { flex: none; width: 8px; height: 8px; margin-top: 2px; }

  .watermark {
    position: absolute;
    left: 230px;
    top: 470px;
    width: 190px;
    height: 190px;
    border-radius: 50%;
    background: var(--tint-green);
  }
</style>
</head>
<body>
  <main class="letterhead">
    <div class="bar bar--top-left"></div>

    <div class="brand">
      <span class="brand__mark"></span>
      <span class="brand__name">Marwick Care Group</span>
    </div>

    <div class="bar bar--header-green"></div>

    <div class="tint tint--a"></div>
    <div class="tint tint--b"></div>
    <div class="tint tint--c"></div>
    <div class="tint tint--d"></div>

    <ul class="contact">
      <li class="contact__item">
        <svg class="contact__icon" viewBox="0 0 10 10" aria-hidden="true"><rect width="10" height="10" rx="2" fill="#5a8ff0"/><path d="M5 2.2a2 2 0 0 0-2 2c0 1.5 2 3.6 2 3.6s2-2.1 2-3.6a2 2 0 0 0-2-2z" fill="#fff"/></svg>
        <span>12 Harbor Lane, Suite 210,<br>Stamford CT 06902</span>
      </li>
      <li class="contact__item">
        <svg class="contact__icon" viewBox="0 0 10 10" aria-hidden="true"><rect width="10" height="10" rx="2" fill="#5a8ff0"/><path d="M3 2.3l1.2 1.6-.6.8a4 4 0 0 0 1.7 1.7l.8-.6L7.7 7 7 7.8C4.8 7.6 2.4 5.2 2.2 3z" fill="#fff"/></svg>
        <span>(203) 555-0147</span>
      </li>
      <li class="contact__item">
        <svg class="contact__icon" viewBox="0 0 10 10" aria-hidden="true"><rect width="10" height="10" rx="2" fill="#5a8ff0"/><circle cx="5" cy="5" r="2.6" fill="none" stroke="#fff" stroke-width="0.9"/><path d="M2.4 5h5.2M5 2.4v5.2" stroke="#fff" stroke-width="0.7"/></svg>
        <span>www.marwickcaregroup.example</span>
      </li>
    </ul>

    <div class="bar bar--header-blue"></div>

    <div class="watermark" role="img" aria-label="Faint brand emblem watermark"></div>

    <div class="bar bar--footer-blue"></div>
    <div class="bar bar--footer-green"></div>
  </main>
</body>
</html>
```